新しくオープンしたラーメン居酒屋の新メニューのチラシ制作をお願いします。
こだわりが強く、比較的高級なラーメン屋です。高級感のある本格的なデザイン、訴求力がありながらも上品なデザインを希望します。
サイズ:A4サイズ
ノビテルで入稿します。
編集できるイラストレーターとPDFファイルでの納品をお願いします。

イメージ通りでした。

この度はたくさんのご応募ありがとうございます。今後ともよろしくお願いいたします。

```html
<!DOCTYPE html>
<html lang="ja">
<head>
<meta charset="utf-8">
<title>夏季限定 冷製 鯛出汁塩山椒そば</title>
<link href="https://fonts.googleapis.com/css2?family=Shippori+Mincho:wght@500;700&family=Yuji+Boku&display=swap" rel="stylesheet">
<style>
  :root {
    --ink: #0b0908;
    --ink-soft: #1a1410;
    --gold: #c9a25a;
    --gold-deep: #7a5a28;
    --cream: #f4ecd8;
    --broth: #d9c08a;
    --red: #d0121b;
    --white: #ffffff;
  }
  * { margin: 0; padding: 0; box-sizing: border-box; }
  html, body { width: 846px; height: 1200px; overflow: hidden; background: var(--ink); }
  .flyer {
    position: relative;
    width: 846px;
    height: 1200px;
    overflow: hidden;
    background: radial-gradient(ellipse at 30% 85%, var(--ink-soft) 0%, var(--ink) 70%);
    font-family: "Shippori Mincho", serif;
    color: var(--white);
  }
  .dish-photo {
    position: absolute;
    left: 0;
    top: 0;
    width: 690px;
    height: 720px;
    background:
      radial-gradient(circle at 52% 48%, var(--cream) 0%, var(--broth) 38%, #a8803f 58%, #3b2a14 76%, var(--ink) 92%);
  }
  .gold-sweep {
    position: absolute;
    left: 0;
    top: 560px;
    width: 846px;
    height: 240px;
  }
  .season-tag {
    position: absolute;
    left: 782px;
    top: 20px;
    writing-mode: vertical-rl;
    font-size: 34px;
    font-weight: 700;
    letter-spacing: 0.08em;
    color: var(--white);
  }
  .dish-name {
    position: absolute;
    left: 680px;
    top: 70px;
    writing-mode: vertical-rl;
    font-family: "Yuji Boku", serif;
    font-size: 90px;
    line-height: 1;
    letter-spacing: 0.02em;
    color: var(--red);
    text-shadow: 0 0 6px rgba(0,0,0,0.6);
  }
  .dish-name .gap { display: inline-block; height: 0.5em; }
  .description {
    position: absolute;
    left: 54px;
    top: 810px;
    font-size: 30px;
    line-height: 51px;
    font-weight: 500;
    letter-spacing: 0.04em;
  }
  .price {
    position: absolute;
    left: 52px;
    top: 1095px;
    font-size: 64px;
    font-weight: 500;
    letter-spacing: 0.04em;
    color: var(--white);
  }
</style>
</head>
<body>
  <main class="flyer">
    <div class="dish-photo" role="img" aria-label="冷製鯛出汁塩山椒そばの写真：澄んだスープに細麺、海老、梅干し、青菜、豆腐、海苔を盛り付けた器"></div>

    <svg class="gold-sweep" viewBox="0 0 846 240" aria-hidden="true">
      <defs>
        <linearGradient id="sweepGold" x1="0" y1="0" x2="1" y2="0">
          <stop offset="0" stop-color="#7a5a28"/>
          <stop offset="0.45" stop-color="#e2c07a"/>
          <stop offset="1" stop-color="#6b4e22"/>
        </linearGradient>
      </defs>
      <path d="M0 170 Q 330 150 620 90 T 846 20 L 846 44 Q 700 100 620 112 Q 330 172 0 196 Z" fill="url(#sweepGold)" opacity="0.85"/>
      <path d="M0 205 Q 360 185 846 70" stroke="#c9a25a" stroke-width="2" fill="none" opacity="0.45"/>
    </svg>

    <p class="season-tag">夏季限定</p>
    <h1 class="dish-name">冷製<span class="gap"></span>鯛出汁塩山椒そば</h1>

    <p class="description">
      濃密ながら清らかな真鯛出汁、<br>
      香りの異なる２種類の<br>
      山椒を漬け込んだ香味油、<br>
      自家製の塩だれが三位一体となった一杯。<br>
      化学調味料不使用。
    </p>

    <p class="price">￥1,000</p>
  </main>
</body>
</html>
```